STI/STD Medical Clinic- Wellspring Crest Partners, Inc Website

We are a STI clinic in florida looking for a website. We want to be professional but also playful. We want a buildout similar to the website listed below as our clinic is very similar to theirs.

This is a great example of a clinic doing similar stuff as us. We obviously do not want their color scheme but their format and buildout work. Please see our logo attached for color schemes etc.

https://bluefernclinicmiami.org

Industry/Entity Type

Medical

Coding

Coded - Design and coding required

Number of Pages Required

5+ page

Font styles to use
Sans Serif

```html
<!DOCTYPE html>
<html lang="en">
<head>
<meta charset="utf-8">
<title>Wellspring Crest Partners</title>
<link rel="stylesheet" href="https://fonts.googleapis.com/css2?family=Rubik:wght@400;500;600&family=Inter:wght@400;500;600&display=swap">
<style>
:root{
  --blue:#2f5ee6;
  --pink:#f0477a;
  --sky:#1a8fd6;
  --sky-dark:#0b7cc4;
  --navy:#0e4a6e;
  --ink:#1b1e2e;
  --text:#3a3d4c;
  --muted:#6b6f80;
  --soft:#f3f8fd;
  --footer:#23252f;
  --grad:linear-gradient(90deg,#2f5ee6,#f0477a);
}
*{box-sizing:border-box;margin:0;padding:0}
html,body{width:1200px;height:4617px;overflow:hidden}
body{font-family:Inter,sans-serif;color:var(--text);background:#fff;position:relative}
.abs{position:absolute}
h1,h2,h3,.rubik{font-family:Rubik,sans-serif}
.btn{position:absolute;display:flex;align-items:center;justify-content:center;border-radius:24px;background:var(--grad);color:#fff;font-family:Rubik,sans-serif;font-weight:500;font-size:17px}
.eyebrow{position:absolute;font-family:Rubik,sans-serif;font-weight:500;font-size:16px;color:var(--blue)}
.title{position:absolute;font-family:Rubik,sans-serif;font-weight:500;color:var(--ink)}
.center{left:0;width:1200px;text-align:center}

/* top bar + nav */
.promo{left:0;top:0;width:1200px;height:21px;background:var(--grad);color:#fff;font-size:11px;font-weight:500;display:flex;align-items:center;justify-content:center}
.nav{left:0;top:21px;width:1200px;height:72px;background:#fff}
.brand{position:absolute;display:flex;align-items:center;gap:10px;font-family:Rubik,sans-serif;font-weight:600;font-size:22px;color:var(--blue)}
.brand i{display:block;width:30px;height:30px;border-radius:50%;background:var(--blue)}
.nav-links{position:absolute;left:449px;top:27px;display:flex;gap:26px;font-size:14px;color:var(--ink)}
.portal{position:absolute;left:887px;top:19px;width:183px;height:42px;border:2px solid var(--blue);border-radius:22px;color:var(--blue);font-family:Rubik,sans-serif;font-weight:500;font-size:17px;display:flex;align-items:center;justify-content:center;gap:8px}

/* hero */
.hero{left:0;top:93px;width:1200px;height:561px;background:linear-gradient(100deg,#0a5f9e 0%,#1d86c9 45%,#8fb6cf 75%,#d9e4ec 100%)}
.hero-cut{left:0;top:560px}
.hero-kicker{left:130px;top:220px;font-family:Rubik,sans-serif;font-weight:500;font-size:32px;color:#fff}
.hero-title{left:130px;top:252px;font-family:Rubik,sans-serif;font-weight:600;font-size:62px;color:#fff;line-height:1.1}
.hero-text{left:130px;top:349px;width:430px;font-size:14px;line-height:21px;color:#fff}

/* services */
.services{left:0;top:654px;width:1200px;height:640px;background:var(--soft)}
.card{position:absolute;width:205px;height:211px;background:#fff;border:1px solid #dfe4ee;border-radius:8px;text-align:center;padding:0 14px}
.card svg{margin-top:24px}
.card h3{font-size:18px;font-weight:500;color:var(--ink);margin-top:12px;line-height:21px}
.card p{font-size:11px;line-height:16px;color:var(--text);margin-top:10px}

/* visit */
.visit-photo{left:0;top:1293px;width:612px;height:512px;background:linear-gradient(135deg,#eef1f3,#cfd8dd 60%,#8aa08a)}
.visit-panel{left:612px;top:1329px;width:588px;height:476px;background:linear-gradient(135deg,#1a8fd6,#0b78bd)}
.pink-label{position:absolute;font-family:Rubik,sans-serif;font-weight:500;font-size:16px;color:var(--pink)}
.white-title{position:absolute;font-family:Rubik,sans-serif;font-weight:500;color:#fff}
.white-text{position:absolute;font-size:14px;line-height:22px;color:#fff}

/* team */
.doc-photo{position:absolute;width:279px;height:333px;background:linear-gradient(160deg,#e8eef3,#b9c8d3);box-shadow:0 6px 18px rgba(0,0,0,.12)}
.doc-info{position:absolute;width:267px;height:172px;background:#fff;box-shadow:0 10px 24px rgba(20,30,60,.14);text-align:center;padding-top:34px}
.doc-info h3{font-size:17px;font-weight:500;color:var(--ink)}
.doc-info .role{font-size:12px;color:var(--blue);margin-top:4px}
.doc-info p{font-size:11px;line-height:16px;margin:10px 18px 0}
.arrow{position:absolute;width:60px;height:60px;border-radius:50%;display:flex;align-items:center;justify-content:center}

/* about */
.about-photo{left:585px;top:2515px;width:615px;height:533px;background:linear-gradient(135deg,#dfe8ee,#9bb7c8 55%,#4a7e63)}
.about-panel{left:0;top:2574px}
.about-btn{left:130px;top:2916px;width:138px;height:48px;border-radius:24px;background:#fff;color:var(--blue);font-family:Rubik,sans-serif;font-weight:500;font-size:17px;display:flex;align-items:center;justify-content:center}

/* reviews */
.review{position:absolute;width:292px;height:212px;background:#fff;box-shadow:0 6px 22px rgba(20,30,60,.12);padding:24px 20px}
.review.faded{opacity:.45}
.stars{color:#f59a23;font-size:18px;letter-spacing:4px}
.review p{font-size:12px;line-height:21px;margin-top:8px}
.review .g{position:absolute;right:18px;bottom:16px;width:14px;height:14px;border-radius:50%;border:3px solid #4285f4}
.author{position:absolute;display:flex;align-items:center;gap:12px}
.author i{display:block;width:40px;height:40px;border-radius:50%;background:#d9dfe6}
.author b{display:block;font-weight:400;font-size:14px;color:var(--blue)}
.author span{font-size:13px}
.review.faded + .author{opacity:.45}
.dot{position:absolute;width:10px;height:10px;border-radius:50%;background:#c9cdd6}

/* contact */
.map{left:0;top:3764px;width:566px;height:457px;background:linear-gradient(135deg,#f1f1ed,#e3e6e0)}
.field{position:absolute;background:#fff;border-radius:3px;font-size:10px;color:var(--muted);padding:12px 14px}

/* footer */
.footer{left:0;top:4257px;width:1200px;height:360px;background:var(--footer);color:#fff}
.footer h4{position:absolute;font-family:Rubik,sans-serif;font-weight:500;font-size:16px;letter-spacing:.3px}
.footer ul{position:absolute;list-style:none;font-size:14px;line-height:30px;color:#d7d9e2}
.f-contact{position:absolute;display:flex;gap:14px;font-size:14px;line-height:21px;color:#d7d9e2}
.f-contact svg{flex:none;margin-top:2px}
.social{position:absolute;width:26px;height:26px;border-radius:50%;background:var(--grad)}
</style>
</head>
<body>

<div class="abs promo">Special Offer 50% Discount Today</div>

<header class="abs nav">
  <div class="brand" style="left:130px;top:20px"><i></i>Wellspring Crest</div>
  <nav class="nav-links"><span>Home</span><span>About</span><span>Meet The Team</span><span>Services</span><span>Contact</span></nav>
  <div class="portal">
    <svg width="14" height="14" viewBox="0 0 14 14"><circle cx="7" cy="4" r="3" fill="#2f5ee6"/><path d="M1 14a6 6 0 0 1 12 0z" fill="#2f5ee6"/></svg>
    Patient Portal
  </div>
</header>

<section>
  <div class="abs hero" role="img" aria-label="Photo of a team of smiling doctors in white coats over a city skyline"></div>
  <svg class="abs hero-cut" width="1200" height="95" viewBox="0 0 1200 95"><polygon points="0,5 1200,94 1200,95 0,95" fill="#f3f8fd"/></svg>
  <div class="abs hero-kicker">WELLSPRING</div>
  <h1 class="abs hero-title">Crest Partners</h1>
  <svg class="abs" style="left:130px;top:321px" width="390" height="6"><rect width="390" height="5" rx="2" fill="#f0477a"/></svg>
  <p class="abs hero-text"><em>Lorem ipsum dolor</em> sit amet, consectetur adipiscing elit. Mattis ipsum vel egestas interdum velit lectus mattis hendrerit. Ut interdum ut facilisis ut amet</p>
  <div class="btn" style="left:130px;top:446px;width:237px;height:45px">Make An Appointment</div>
</section>

<section class="abs services">
  <div class="eyebrow center" style="top:10px">What We Do</div>
  <h2 class="title center" style="top:40px;font-size:38px">Services We Prowide</h2>

  <div class="card" style="left:129px;top:116px"><svg width="64" height="64" viewBox="0 0 64 64" role="img" aria-label="Stethoscope icon"><defs><linearGradient id="ig" x1="0" x2="1"><stop offset="0" stop-color="#2f5ee6"/><stop offset="1" stop-color="#f0477a"/></linearGradient></defs><path d="M16 8v18a12 12 0 0 0 24 0V8M28 38v8a10 10 0 0 0 20 0v-6" fill="none" stroke="url(#ig)" stroke-width="3"/><circle cx="48" cy="36" r="5" fill="none" stroke="url(#ig)" stroke-width="3"/></svg><h3>PrEP</h3><p>Lorem ipsum dolor sit amet, consectetur adipiscing elit. Id blandit sed mattis amet.</p></div>
  <div class="card" style="left:372px;top:116px"><svg width="64" height="64" viewBox="0 0 64 64" role="img" aria-label="Pills icon"><rect x="8" y="14" width="30" height="16" rx="8" transform="rotate(-35 23 22)" fill="none" stroke="url(#ig)" stroke-width="3"/><ellipse cx="40" cy="42" rx="16" ry="9" fill="none" stroke="url(#ig)" stroke-width="3"/></svg><h3>PeP</h3><p>Lorem ipsum dolor sit amet, consectetur adipiscing elit. Id blandit sed mattis amet.</p></div>
  <div class="card" style="left:615px;top:116px"><svg width="64" height="64" viewBox="0 0 64 64" role="img" aria-label="Liver icon"><path d="M8 20c10-8 36-10 48-4 4 10-8 22-20 26-6 2-8 10-8 14-10-8-22-20-20-36z" fill="none" stroke="url(#ig)" stroke-width="3"/></svg><h3>Hepatitis C</h3><p>Lorem ipsum dolor sit amet, consectetur adipiscing elit. Id blandit sed mattis amet.</p></div>
  <div class="card" style="left:858px;top:116px"><svg width="64" height="64" viewBox="0 0 64 64" role="img" aria-label="Awareness ribbon icon"><path d="M32 8c-8 0-10 10-4 20l-12 26M32 8c8 0 10 10 4 20l12 26M24 40h16" fill="none" stroke="url(#ig)" stroke-width="3"/></svg><h3>HIV</h3><p>Lorem ipsum dolor sit amet, consectetur adipiscing elit. Id blandit sed mattis amet.</p></div>

  <div class="card" style="left:129px;top:360px"><svg width="64" height="64" viewBox="0 0 64 64" role="img" aria-label="Condom pack icon"><rect x="8" y="8" width="48" height="48" rx="4" fill="none" stroke="url(#ig)" stroke-width="3"/><circle cx="32" cy="32" r="13" fill="none" stroke="url(#ig)" stroke-width="3"/><circle cx="32" cy="32" r="7" fill="none" stroke="url(#ig)" stroke-width="3"/></svg><h3>STI</h3><p>Lorem ipsum dolor sit amet, consectetur adipiscing elit. Id blandit sed mattis amet.</p></div>
  <div class="card" style="left:372px;top:360px"><svg width="64" height="64" viewBox="0 0 64 64" role="img" aria-label="Clipboard icon"><rect x="10" y="10" width="38" height="46" rx="3" fill="none" stroke="url(#ig)" stroke-width="3"/><path d="M18 24h22M18 34h22M18 44h14M44 48l12-18" fill="none" stroke="url(#ig)" stroke-width="3"/></svg><h3>Case Management</h3><p>Lorem ipsum dolor sit amet, consectetur adipiscing elit. Id blandit sed mattis amet.</p></div>
  <div class="card" style="left:615px;top:360px"><svg width="64" height="64" viewBox="0 0 64 64" role="img" aria-label="Phone with medical cross icon"><rect x="20" y="6" width="28" height="50" rx="4" fill="none" stroke="url(#ig)" stroke-width="3"/><rect x="8" y="26" width="22" height="22" rx="3" fill="#fff" stroke="url(#ig)" stroke-width="3"/><path d="M19 31v12M13 37h12" stroke="url(#ig)" stroke-width="3"/></svg><h3>Telehealth</h3><p>Lorem ipsum dolor sit amet, consectetur adipiscing elit. Id blandit sed mattis amet.</p></div>
  <div class="card" style="left:858px;top:360px"><svg width="64" height="52" viewBox="0 0 64 52" role="img" aria-label="Speech bubbles icon"><path d="M6 6h34v22H20l-8 8v-8H6z" fill="none" stroke="url(#ig)" stroke-width="3"/><path d="M28 20h30v20h-6v8l-8-8H28z" fill="none" stroke="url(#ig)" stroke-width="3"/></svg><h3>Language Interpretation Services</h3><p>Lorem ipsum dolor sit amet.</p></div>
</section>

<section>
  <div class="abs visit-photo" role="img" aria-label="Photo of a smiling female doctor at her desk with a laptop"></div>
  <div class="abs visit-panel"></div>
  <div class="pink-label" style="left:668px;top:1437px">Make An Appointment</div>
  <h2 class="white-title" style="left:668px;top:1462px;font-size:40px">Visit Us Today</h2>
  <p class="white-text" style="left:668px;top:1530px;width:400px">Eget lobortis amet justo nunc. Tortor, ac, sagittis in tortor morbi purus gravida vitae. Platea lectus ut semper dictum scelerisque velit tortor, ornare. Tellus eros tincidunt erat faucibus suspendisse.</p>
  <div class="btn" style="left:668px;top:1653px;width:237px;height:45px">Make An Appointment</div>
</section>

<section>
  <div class="eyebrow center" style="top:1905px">Stuff</div>
  <h2 class="title center" style="top:1925px;font-size:38px">Our Team</h2>

  <div class="doc-photo" style="left:129px;top:1997px" role="img" aria-label="Portrait of a male doctor"></div>
  <div class="doc-info" style="left:163px;top:2210px"><h3>Dr. Nolan Pierce</h3><div class="role">Lorem ipsum</div><p>Lorem ipsum dolor sit amet, consectetur adipiscing elit. Id blandit sed mattis amet scelerisque in risus in.</p></div>

  <div class="doc-photo" style="left:451px;top:1997px" role="img" aria-label="Portrait of a female doctor"></div>
  <div class="doc-info" style="left:485px;top:2210px"><h3>Dr. Maren Hollis</h3><div class="role">Lorem ipsum</div><p>Lorem ipsum dolor sit amet, consectetur adipiscing elit. Id blandit sed mattis amet scelerisque in risus in.</p></div>

  <div class="doc-photo" style="left:773px;top:1997px" role="img" aria-label="Portrait of a female doctor with stethoscope"></div>
  <div class="doc-info" style="left:807px;top:2210px"><h3>Dr. Priya Castell</h3><div class="role">Lorem ipsum</div><p>Lorem ipsum dolor sit amet, consectetur adipiscing elit. Id blandit sed mattis amet scelerisque in risus in.</p></div>

  <div class="arrow" style="left:528px;top:2438px;background:#e6e8ec"><svg width="22" height="14" viewBox="0 0 22 14"><path d="M21 7H2M8 1 2 7l6 6" fill="none" stroke="#1b1e2e" stroke-width="2"/></svg></div>
  <div class="arrow" style="left:610px;top:2438px;background:var(--grad)"><svg width="22" height="14" viewBox="0 0 22 14"><path d="M1 7h19M14 1l6 6-6 6" fill="none" stroke="#fff" stroke-width="2"/></svg></div>
</section>

<section>
  <div class="abs about-photo" role="img" aria-label="Photo of a doctor consulting with two patients"></div>
  <svg class="abs about-panel" width="585" height="474" viewBox="0 0 585 474"><polygon points="0,76 585,0 585,474 0,474" fill="#0e4a6e"/></svg>
  <span class="abs" style="left:130px;top:2706px;width:52px;height:52px;border-radius:50%;background:rgba(255,255,255,.85)"></span>
  <div class="pink-label" style="left:203px;top:2698px">Welcome To Wellspring</div>
  <h2 class="white-title" style="left:203px;top:2722px;font-size:40px">About Us</h2>
  <p class="white-text" style="left:130px;top:2796px;width:380px">Eget lobortis amet justo nunc. Tortor, ac, sagittis in tortor morbi purus gravida vitae. Platea lectus ut semper dictum scelerisque velit tortor, ornare. Tellus eros tincidunt erat faucibus suspendisse.</p>
  <div class="abs about-btn">Read More</div>
</section>

<section>
  <div class="eyebrow center" style="top:3150px">Testimonials</div>
  <h2 class="title center" style="top:3192px;font-size:38px">Happy Patients Reviews</h2>

  <div class="review faded" style="left:-23px;top:3306px"><div class="stars">★★★★★</div><p>Lorem ipsum dolor sit amet, consectetur adipiscing elit. Scelerisque a malesuada egestas non facilisis risus id nisi, tellus. Sed pellentesque iaculis in varius velit. Eget pellentesque libero, turpis tellus nibh ut tellus.</p><span class="g"></span></div>
  <div class="author" style="left:-23px;top:3534px;opacity:.45"><i></i><div><b>Lena Marsh</b><span>Lorem ipsum</span></div></div>

  <div class="review" style="left:296px;top:3281px"><div class="stars">★★★★★</div><p>Lorem ipsum dolor sit amet, consectetur adipiscing elit. Scelerisque a malesuada egestas non facilisis risus id nisi, tellus. Sed pellentesque iaculis in varius velit. Eget pellentesque libero, turpis tellus nibh ut tellus.</p><span class="g"></span></div>
  <div class="author" style="left:298px;top:3510px"><i></i><div><b>Lena Marsh</b><span>Lorem ipsum</span></div></div>

  <div class="review" style="left:631px;top:3281px"><div class="stars">★★★★★</div><p>Lorem ipsum dolor sit amet, consectetur adipiscing elit. Scelerisque a malesuada egestas non facilisis risus id nisi, tellus. Sed pellentesque iaculis in varius velit. Eget pellentesque libero, turpis tellus nibh ut tellus.</p><span class="g"></span></div>
  <div class="author" style="left:633px;top:3510px"><i></i><div><b>Lena Marsh</b><span>Lorem ipsum</span></div></div>

  <div class="review faded" style="left:966px;top:3306px"><div class="stars">★★★★★</div><p>Lorem ipsum dolor sit amet, consectetur adipiscing elit. Scelerisque a malesuada egestas non facilisis risus id nisi, tellus. Sed pellentesque iaculis in varius velit. Eget pellentesque libero, turpis tellus nibh ut tellus.</p><span class="g"></span></div>
  <div class="author" style="left:966px;top:3534px;opacity:.45"><i></i><div><b>Lena Marsh</b><span>Lorem ipsum</span></div></div>

  <span class="dot" style="left:574px;top:3622px;background:var(--blue)"></span>
  <span class="dot" style="left:595px;top:3622px"></span>
  <span class="dot" style="left:616px;top:3622px"></span>
</section>

<section>
  <svg class="abs" style="left:0;top:3731px" width="1200" height="490" viewBox="0 0 1200 490"><defs><linearGradient id="cg" x1="0" x2="1" y1="0" y2="1"><stop offset="0" stop-color="#1a8fd6"/><stop offset="1" stop-color="#0b78bd"/></linearGradient></defs><path d="M420 0H1200V490H0V60H300C340 20 380 0 420 0z" fill="url(#cg)"/></svg>
  <div class="abs map" role="img" aria-label="Street map showing the clinic location marker"></div>
  <div class="pink-label" style="left:612px;top:3803px">Contact Us</div>
  <h2 class="white-title" style="left:612px;top:3826px;font-size:38px;line-height:46px">Let Us assist you &amp;<br>Your love ones</h2>
  <div class="field" style="left:614px;top:3947px;width:194px;height:38px">Name *</div>
  <div class="field" style="left:823px;top:3947px;width:195px;height:38px">Phone *</div>
  <div class="field" style="left:614px;top:3996px;width:404px;height:38px">Email *</div>
  <div class="field" style="left:614px;top:4045px;width:404px;height:68px">How we can help?</div>
  <div class="btn" style="left:614px;top:4136px;width:110px;height:46px">Submit</div>
</section>

<footer class="abs footer">
  <div class="brand" style="left:130px;top:62px;color:#fff"><i></i>Wellspring Crest</div>
  <h3 class="abs" style="left:130px;top:168px;font-size:18px;font-weight:400">Working Hours</h3>
  <span class="abs" style="left:130px;top:198px;width:90px;height:3px;background:var(--grad)"></span>
  <p class="abs" style="left:130px;top:212px;font-size:14px;line-height:30px;color:#d7d9e2">Mn – Fr : <b style="color:#fff;font-weight:500">8:00 am – 6:30 pm</b><br>Sat – Su : <b style="color:#fff;font-weight:500">9:00 am – 3:00 pm</b></p>

  <h4 style="left:418px;top:74px">USEFULL LINKS</h4>
  <span class="abs" style="left:418px;top:100px;width:60px;height:3px;background:var(--grad)"></span>
  <ul style="left:418px;top:116px"><li>About</li><li>Meet The Team</li><li>Services</li><li>Contact</li></ul>

  <h4 style="left:614px;top:74px">PATIENT PORTAL</h4>
  <span class="abs" style="left:614px;top:100px;width:60px;height:3px;background:var(--grad)"></span>
  <ul style="left:614px;top:116px"><li>Login</li><li>Sign Up</li><li>Privacy Policy</li><li>&nbsp;Terms and Conditions</li></ul>

  <h4 style="left:827px;top:74px">CONTACT INFORMATION</h4>
  <span class="abs" style="left:827px;top:100px;width:60px;height:3px;background:var(--grad)"></span>
  <div class="f-contact" style="left:827px;top:121px"><svg width="16" height="18" viewBox="0 0 16 18"><path d="M8 17s6-6 6-10A6 6 0 0 0 2 7c0 4 6 10 6 10z" fill="none" stroke="#f0477a" stroke-width="1.6"/><circle cx="8" cy="7" r="2" fill="#f0477a"/></svg><span>2208 Coral Ridge Blvd.<br>Tampa, Florida 33602</span></div>
  <div class="f-contact" style="left:827px;top:178px"><svg width="16" height="16" viewBox="0 0 16 16"><path d="M3 1h3l1.5 4-2 1.2a9 9 0 0 0 4.3 4.3L11 8.5l4 1.5v3a2 2 0 0 1-2 2A13 13 0 0 1 1 3a2 2 0 0 1 2-2z" fill="none" stroke="#f0477a" stroke-width="1.5"/></svg><span>(813) 555-0164</span></div>
  <div class="f-contact" style="left:827px;top:210px"><svg width="16" height="14" viewBox="0 0 16 14"><rect x="1" y="1.5" width="14" height="11" rx="1.5" fill="none" stroke="#f0477a" stroke-width="1.5"/><path d="m1.5 2.5 6.5 5 6.5-5" fill="none" stroke="#f0477a" stroke-width="1.5"/></svg><span>hello@wellspringcrest.org</span></div>

  <span class="abs" style="left:130px;top:296px;width:940px;height:1px;background:#44475a"></span>
  <p class="abs" style="left:130px;top:320px;font-size:11px;color:#d7d9e2">©Copyright 2022. <span style="color:var(--blue);text-decoration:underline">Wellspring Crest Partners, Inc</span> | All Rights Reserved</p>
  <span class="social" style="left:917px;top:315px"></span>
  <span class="social" style="left:959px;top:315px"></span>
  <span class="social" style="left:1000px;top:315px"></span>
  <span class="social" style="left:1041px;top:315px"></span>
</footer>

</body>
</html>
```